Stonebay Towing Business Card

Towing
Accident towing
Mechanical breakdown
Insurance, salvage and recovery
4wd off road towing
Light & Heavy towing
8347 2516
24 hour business 7 days

Logo can be whole size on front

Industry/Entity Type

Towing/ transport

Contact Information for Business Card

The above

```html
<!DOCTYPE html>
<html lang="en">
<head>
<meta charset="utf-8">
<title>Stonebay Towing Business Card</title>
<link href="https://fonts.googleapis.com/css2?family=Oswald:wght@400;600;700&display=swap" rel="stylesheet">
<style>
  :root {
    --backdrop: #adadad;
    --card-dark: #242424;
    --card-dark-ink: #161616;
    --card-light: #ffffff;
    --brand-red: #d42028;
    --ink: #111111;
    --white: #ffffff;
  }
  * { margin: 0; padding: 0; box-sizing: border-box; }
  html, body {
    width: 1200px;
    height: 1000px;
    overflow: hidden;
    background: var(--backdrop);
    font-family: "Oswald", sans-serif;
  }
  .card {
    position: absolute;
    width: 694px;
    height: 398px;
    border-radius: 26px;
    overflow: hidden;
    box-shadow: 6px 6px 10px rgba(0,0,0,0.25);
  }
  .card-front {
    left: 248px;
    top: 86px;
    background: var(--card-dark);
    display: flex;
    align-items: center;
    justify-content: center;
  }
  .front-name {
    font-family: "Oswald", sans-serif;
    font-weight: 600;
    font-size: 84px;
    letter-spacing: 1px;
    color: var(--card-dark-ink);
    text-transform: none;
  }
  .card-back {
    left: 251px;
    top: 530px;
    background: var(--card-light);
  }
  .service-list {
    position: absolute;
    left: 52px;
    top: 38px;
    list-style: none;
  }
  .service-list li {
    font-weight: 400;
    font-size: 28px;
    line-height: 35px;
    color: var(--ink);
    padding-left: 20px;
    position: relative;
  }
  .service-list li::before {
    content: "";
    position: absolute;
    left: 0;
    top: 15px;
    width: 9px;
    height: 9px;
    border-radius: 50%;
    background: var(--brand-red);
  }
  .back-name {
    position: absolute;
    right: 46px;
    top: 48px;
    font-weight: 600;
    font-size: 34px;
    color: var(--brand-red);
  }
  .footer-wave {
    position: absolute;
    left: 0;
    top: 0;
    width: 694px;
    height: 398px;
  }
  .hours {
    position: absolute;
    left: 99px;
    top: 326px;
    font-weight: 700;
    font-size: 42px;
    line-height: 50px;
    color: var(--white);
  }
  .phone {
    position: absolute;
    right: 38px;
    top: 328px;
    font-weight: 700;
    font-size: 42px;
    line-height: 50px;
    color: var(--white);
    letter-spacing: 0.5px;
  }
</style>
</head>
<body>
  <section class="card card-front">
    <span class="front-name">Stonebay Towing</span>
  </section>

  <section class="card card-back">
    <ul class="service-list">
      <li>Towing</li>
      <li>Accident towing</li>
      <li>Mechanical breakdown</li>
      <li>Insurance, salvage and recovery</li>
      <li>4wd off road towing</li>
      <li>Light &amp; Heavy towing</li>
    </ul>

    <span class="back-name">Stonebay Towing</span>

    <svg class="footer-wave" viewBox="0 0 694 398" aria-hidden="true">
      <path d="M0 324 C 50 295, 110 278, 160 278 C 300 280, 470 318, 583 320 C 630 321, 670 315, 694 302 L694 398 L0 398 Z" fill="var(--brand-red)"/>
      <path d="M0 324 C 50 295, 110 278, 160 278 C 300 280, 470 318, 583 320 C 630 321, 670 315, 694 302" fill="none" stroke="var(--ink)" stroke-width="4"/>
      <g class="clock-icon">
        <circle cx="72" cy="354" r="20" fill="none" stroke="var(--ink)" stroke-width="3"/>
        <path d="M72 340 V355 L64 364" fill="none" stroke="var(--ink)" stroke-width="2.5" stroke-linecap="round"/>
      </g>
      <g class="phone-icon">
        <circle cx="427" cy="355" r="20" fill="var(--ink)"/>
        <path d="M420 346 c-3 2 -3 6 0 11 c3 5 7 8 11 8 c2 0 3 -2 3 -3 l-4 -3 l-2 2 c-2 -1 -5 -4 -6 -6 l2 -2 l-3 -4 c-1 -1 -1 -1 -1 -3 z" fill="var(--brand-red)"/>
      </g>
    </svg>

    <span class="hours">24/7</span>
    <span class="phone">8347 2516</span>
  </section>
</body>
</html>
```